ad resembling music album cover needed for medical practice

We would like an advertisement that looks like a classic music album cover. Any time period is fine, preferably one that resembles a highly recognizable artist/cover.
Must include male (Dr. Whitcombe) and the logo. Female is good to include, but not necessary. We are a family practice that is open everyday with evening and weekend appointments. While this is an ad for a medical practice, NOT looking like a typical healthcare ad is very important. We are open to a design that would be a "new" ablum/cd/etc cover, but looks like it might be for music....
Updates

Reason: we like the designs.. would like more !!

Target Market(s)

adults 18 to 100+

Industry/Entity Type

Healthcare

Font styles to use
Serif
Sans Serif
Script

Colors

Designer to choose colors to be used in the design.

Requirements
Must have
• Must include our tag line (without ") "Modern Medicine, Traditional Care"
• address: 41735 Larkfield Drive, Suite 210, Mission Viejo, CA 92691
• phone: 949-555-0187
• website: www.pinecrestclinic.example
Nice to have
• creativity!
• An ad that is good for a full page and one for a quarter page that doesn't sacrifice your work!
• nice to include: Family Practice, Open Daily, Book Online, Walk-Ins Welcome
Should not have
• cut/paste over existing album covers, looks like a medical / healthcare ad

```html
<!DOCTYPE html>
<html lang="en">
<head>
<meta charset="utf-8">
<title>Pinecrest Medical Group – Modern Medicine, Traditional Care</title>
<link rel="stylesheet" href="https://fonts.googleapis.com/css2?family=Playfair+Display:ital,wght@1,800;1,900&family=Oswald:wght@300;400&family=Josefin+Sans:wght@600&display=swap">
<style>
  :root {
    --paper: #f4fbf8;
    --sky: #bfe6ec;
    --ocean: #2a7fc4;
    --deep-blue: #1f5fae;
    --violet: #7b3f9c;
    --plum: #6b2a7a;
    --magenta: #c0307a;
    --rose: #de4f93;
    --blush: #f3c6dc;
    --logo-slate: #3f5a70;
  }
  * { margin: 0; padding: 0; box-sizing: border-box; }
  html, body {
    width: 1200px;
    height: 1200px;
    overflow: hidden;
    background: var(--paper);
  }
  .album-cover {
    position: relative;
    width: 1200px;
    height: 1200px;
    overflow: hidden;
    background:
      radial-gradient(ellipse 420px 520px at 40px 420px, rgba(42,127,196,0.85), rgba(42,127,196,0) 70%),
      radial-gradient(ellipse 360px 300px at 60px 900px, rgba(123,63,156,0.55), rgba(123,63,156,0) 70%),
      radial-gradient(ellipse 300px 200px at 1050px 20px, rgba(31,95,174,0.7), rgba(31,95,174,0) 70%),
      radial-gradient(ellipse 360px 220px at 1120px 1100px, rgba(192,48,122,0.45), rgba(192,48,122,0) 70%),
      radial-gradient(ellipse 500px 260px at 200px 1180px, rgba(222,79,147,0.35), rgba(222,79,147,0) 70%),
      radial-gradient(ellipse 700px 600px at 620px 500px, #ffffff, rgba(255,255,255,0) 75%),
      linear-gradient(160deg, var(--sky) 0%, var(--paper) 45%, var(--blush) 100%);
  }
  .brand {
    position: absolute;
    left: 36px;
    top: 46px;
    display: flex;
    align-items: center;
    gap: 14px;
    color: var(--logo-slate);
    font-family: "Josefin Sans", sans-serif;
    font-weight: 600;
    font-size: 40px;
    letter-spacing: 0.5px;
  }
  .brand-square {
    width: 66px;
    height: 66px;
    background: var(--logo-slate);
  }
  .portrait {
    position: absolute;
  }
  .portrait-lead {
    left: 184px;
    top: 160px;
    width: 664px;
    height: 712px;
    border-radius: 46% 46% 8% 8% / 40% 40% 6% 6%;
    background:
      radial-gradient(ellipse 190px 240px at 50% 42%, #fff2b8, rgba(255,230,170,0) 80%),
      linear-gradient(180deg, #b8557a 0%, #e0728f 45%, #c43d6f 75%, rgba(244,210,225,0.2) 100%);
    opacity: 0.9;
  }
  .portrait-partner {
    left: 792px;
    top: 108px;
    width: 208px;
    height: 524px;
    border-radius: 48% 48% 10% 10% / 30% 30% 6% 6%;
    background:
      radial-gradient(ellipse 70px 90px at 50% 26%, #fbe4d8, rgba(251,228,216,0) 80%),
      linear-gradient(180deg, #5a2a4e 0%, #6a3a7a 45%, #5c3d8c 80%, rgba(255,255,255,0) 100%);
    opacity: 0.85;
  }
  .tagline {
    position: absolute;
    left: 0;
    top: 862px;
    width: 1150px;
    text-align: center;
    font-family: "Playfair Display", serif;
    font-style: italic;
    font-weight: 900;
    font-size: 112px;
    line-height: 104px;
    letter-spacing: -1px;
    background: linear-gradient(90deg, var(--magenta) 0%, var(--rose) 30%, var(--plum) 65%, var(--rose) 100%);
    -webkit-background-clip: text;
    background-clip: text;
    color: transparent;
  }
  .contact {
    position: absolute;
    left: 0;
    width: 1180px;
    text-align: center;
    font-family: "Oswald", sans-serif;
    font-weight: 300;
    font-size: 22px;
    letter-spacing: 4.6px;
    color: var(--rose);
  }
  .contact-address { top: 1104px; }
  .contact-reach {
    top: 1138px;
    word-spacing: 6px;
  }
  .contact-reach .gap { display: inline-block; width: 60px; }
  .services {
    position: absolute;
    left: 1158px;
    top: 1182px;
    width: 1160px;
    transform: rotate(-90deg);
    transform-origin: 0 0;
    font-family: "Playfair Display", serif;
    font-style: italic;
    font-weight: 800;
    font-size: 31px;
    white-space: nowrap;
    color: var(--magenta);
    opacity: 0.85;
  }
</style>
</head>
<body>
  <main class="album-cover">
    <div class="brand">
      <span class="brand-square"></span>
      <span class="brand-name">Pinecrest Medical Group</span>
    </div>

    <div class="portrait portrait-lead" role="img" aria-label="Painted watercolour portrait of Dr. Whitcombe, smiling, in a suit and tie"></div>
    <div class="portrait portrait-partner" role="img" aria-label="Painted watercolour portrait of a smiling female physician in a polka-dot blouse"></div>

    <h1 class="tagline">Modern Medicine,<br>Traditional Care</h1>

    <p class="contact contact-address">41735 Larkfield Drive, Suite 210, Mission Viejo, CA 92691</p>
    <p class="contact contact-reach">Call 949-555-0187<span class="gap"></span>www.pinecrestclinic.example</p>

    <p class="services">Family Practice, Open Daily, Book Online, Walk-Ins Welcome</p>
  </main>
</body>
</html>
```